Ecommerce Website For Printing Company

Quillbrook.com are a print, design and signage company who sell flyers, business cards, posters, brochures and more to customers in the UK.

Our website is outdated and requires a new design using current web styling and mobile functionality.

We require the following pages to be designed;
- Home Page
- Price Page
- Portfolio Page
- Blog
- Content Page

Our competitors in the printing industry are www.venturaprint.com, www.lanternpress.co.uk, gableinkworks.co.uk, www.paperhaven.co.uk

We require the website to give a professional image as well as be easy for customers to navigate, understand and find prices.

Target Market(s)

Businesses

Industry/Entity Type

Printing

Number of Pages Required

4 page

Font styles to use
Sans Serif

Colors
33a6d7

Requirements
Must have
• Popular products, latest news/blog, sales from portfolio, newsletter sign up, footer

```html
<!DOCTYPE html>
<html lang="en">
<head>
<meta charset="utf-8">
<title>Quillbrook.com – Print, Design &amp; Signage</title>
<link href="https://fonts.googleapis.com/css2?family=Roboto:wght@300;400;500;700&family=Roboto+Condensed:wght@400;700&display=swap" rel="stylesheet">
<style>
:root{
  --brand:#33a6d7;
  --brand-dark:#1f86b8;
  --brand-light:#e6f4fb;
  --ink:#333b40;
  --muted:#7a858c;
  --line:#d6e8f1;
  --white:#ffffff;
  --footer:#3aa9d9;
  --footer-dark:#2a95c4;
}
*{box-sizing:border-box;margin:0;padding:0}
html,body{width:1200px;height:3648px;overflow:hidden}
body{font-family:'Roboto',Arial,sans-serif;color:var(--ink);background:var(--white);position:relative}
.wrap{width:1056px;margin:0 auto;position:relative}
section,header,footer{position:absolute;left:0;width:1200px}

/* header */
.site-header{top:0;height:152px;background:var(--white)}
.logo{position:absolute;left:72px;top:22px;display:flex;align-items:center;gap:12px;font-size:40px;font-weight:700;color:var(--brand);letter-spacing:-0.5px}
.logo-mark{width:22px;height:22px;background:var(--brand)}
.main-nav{position:absolute;right:72px;top:34px;display:flex;gap:6px}
.main-nav a{font-size:16px;color:var(--ink);text-decoration:none;padding:10px 16px}
.main-nav a.active{background:var(--brand);color:var(--white)}
.contact-strip{position:absolute;right:72px;top:106px;height:34px;background:var(--brand);display:flex;align-items:center;gap:28px;padding:0 22px 0 36px;color:var(--white);font-size:15px}
.contact-strip span{display:flex;align-items:center;gap:8px}

/* hero */
.hero{top:152px;height:448px;background:linear-gradient(135deg,#cfdde6 0%,#a9c3d3 45%,#5f8ea9 100%)}
.hero-badge{position:absolute;left:490px;top:114px;width:220px;height:220px;border-radius:50%;background:rgba(51,166,215,.92);border:6px solid rgba(255,255,255,.55);display:flex;align-items:center;justify-content:center;text-align:center;color:var(--white);font-family:'Roboto Condensed',Arial,sans-serif;font-size:26px;letter-spacing:2px;line-height:1.3}
.slider-dots{position:absolute;left:0;right:0;bottom:18px;display:flex;justify-content:center;gap:8px}
.slider-dots i{width:12px;height:12px;border-radius:50%;background:rgba(255,255,255,.6)}
.slider-dots i.on{background:var(--brand)}

/* section headings */
.row-head{display:flex;justify-content:space-between;align-items:center;border-bottom:2px solid var(--line);padding-bottom:10px}
.row-head h2{font-family:'Roboto Condensed',Arial,sans-serif;font-weight:400;color:var(--brand);font-size:34px;text-transform:uppercase}
.row-head h3{font-size:20px;font-weight:500;color:var(--ink)}
.arrows{display:flex;gap:8px}
.arrows span{width:28px;height:28px;border-radius:50%;display:flex;align-items:center;justify-content:center}
.arrows .prev{background:#9aa6ad}
.arrows .next{background:var(--brand)}

/* products */
.products{top:600px;height:400px}
.products .wrap{top:60px}
.product-row{display:flex;gap:20px;margin-top:26px}
.product-tile{width:195px;height:220px;border:1px solid var(--line)}
.tile-cards{background:linear-gradient(135deg,#16384d,#2f7fa8)}
.tile-flyers{background:var(--brand);color:var(--white);display:flex;flex-direction:column;align-items:center;justify-content:center;gap:8px;text-align:center}
.tile-flyers strong{font-size:32px;font-weight:500;letter-spacing:1px}
.tile-flyers b{font-size:28px;font-weight:500}
.tile-flyers a{color:var(--white);font-size:15px;border-bottom:1px solid var(--white);text-decoration:none}
.tile-letterhead{background:linear-gradient(160deg,#f2f4f5,#d7dde1)}
.tile-leaflet{background:linear-gradient(135deg,#c7d8e3,#6f93ad)}
.tile-brochure{background:linear-gradient(135deg,#f4f1ec,#d7a9a0 55%,#6aa0c7)}

/* design team */
.design-team{top:1000px;height:320px;background:linear-gradient(90deg,#3b3f42 0%,#5c6166 50%,#2e3134 100%);color:var(--white);text-align:center}
.design-team h2{margin-top:60px;font-size:34px;font-weight:500}
.design-team p{width:560px;margin:22px auto 0;font-size:18px;line-height:1.55;font-weight:300}
.btn-outline{display:inline-block;margin-top:30px;border:2px solid var(--white);color:var(--white);padding:14px 40px;font-size:16px;text-decoration:none}

/* portfolio */
.portfolio{top:1320px;height:1100px}
.portfolio .title{text-align:center;font-size:36px;font-weight:400;color:var(--brand);margin-top:80px}
.portfolio .row-head{margin-top:46px}
.portfolio .row-head.second{margin-top:54px}
.folio-row{display:flex;gap:24px;margin-top:26px}
.folio-tile{width:246px;height:296px;border:4px solid var(--brand-light);box-shadow:0 0 0 1px var(--line)}
.folio-blue{background:linear-gradient(160deg,#7ccbe9,#33a6d7)}
.folio-cafe{background:linear-gradient(160deg,#f1e8de,#9c7a5c)}
.folio-office{background:linear-gradient(160deg,#eef3f6,#8fb3c8)}
.folio-fitness{background:linear-gradient(160deg,#f3f6f8,#d9a2a0 60%,#33a6d7)}
.folio-flyer{background:linear-gradient(160deg,#f6f3e9,#c9b98c)}
.folio-teal{background:linear-gradient(160deg,#3fb0c9,#1c5c7a)}
.folio-heart{background:linear-gradient(160deg,#e6462f,#a8131a)}
.folio-run{background:linear-gradient(160deg,#f28c28,#6bbf3a)}
.template-label{display:flex;align-items:center;justify-content:center;height:100%;color:var(--white);font-size:24px;font-weight:500}
.view-all{position:absolute;left:508px;top:1008px;width:184px;height:56px;border:2px solid var(--brand);color:var(--brand);display:flex;align-items:center;justify-content:center;font-size:17px;text-decoration:none}

/* blog */
.blog{top:2420px;height:520px;background:var(--brand);overflow:hidden}
.blog svg.bands{position:absolute;left:0;top:0}
.blog h2{position:relative;text-align:center;color:var(--white);font-size:36px;font-weight:400;margin-top:54px}
.blog-row{position:relative;display:flex;gap:24px;margin-top:40px}
.post{width:336px}
.post-img{height:200px}
.post-1{background:linear-gradient(135deg,#2a2d30,#8a9196)}
.post-2{background:linear-gradient(135deg,#2c5f8a,#9fc4dc)}
.post-3{background:linear-gradient(135deg,#cfd6db,#6f8795)}
.post-date{background:var(--white);color:var(--ink);text-align:center;font-size:14px;padding:8px 0}
.post-title{display:block;text-align:center;color:var(--white);font-size:20px;margin-top:22px;text-decoration:underline;line-height:1.3}

/* newsletter */
.newsletter{top:2940px;height:160px;text-align:center}
.newsletter h2{font-size:36px;font-weight:400;color:var(--brand);margin-top:28px}
.signup{display:flex;justify-content:center;margin-top:26px}
.signup input{width:310px;height:44px;border:2px solid var(--brand);padding:0 14px;font-family:inherit;font-size:15px;color:var(--muted)}
.signup button{width:150px;height:44px;background:var(--brand);color:var(--white);border:0;font-family:inherit;font-size:16px;margin-left:12px}

/* footer */
.site-footer{top:3100px;height:548px;background:var(--footer);color:var(--white)}
.footer-cols{display:flex;margin-top:44px}
.footer-col{width:264px}
.footer-col h4{font-size:19px;font-weight:500;margin-bottom:22px}
.news-item{display:flex;gap:12px;margin-bottom:22px;font-size:13px;line-height:1.5}
.news-thumb{width:56px;height:40px;background:rgba(255,255,255,.35);flex:none}
.news-item a{color:var(--white)}
.links li{list-style:none;font-size:13px;line-height:1.95}
.links li::before{content:"›";margin-right:8px}
.cards{display:grid;grid-template-columns:repeat(4,44px);gap:10px}
.cards i{height:28px;background:var(--white);border-radius:3px;opacity:.9}
.touch p{display:flex;gap:12px;font-size:13px;line-height:1.5;margin-bottom:16px}
.touch svg{flex:none;margin-top:2px}
.social{display:flex;gap:12px;margin-top:12px;padding-left:26px}
.social i{width:22px;height:22px;border-radius:50%;background:var(--white);opacity:.85}
.footer-bottom{position:absolute;left:0;right:0;top:440px;border-top:1px solid rgba(255,255,255,.35);text-align:center;font-size:12px;padding-top:18px}
.footer-bottom nav{display:flex;justify-content:center;gap:24px;margin-bottom:12px}
.footer-bottom nav a{color:var(--white);text-decoration:underline}
</style>
</head>
<body>

<header class="site-header">
  <div class="logo"><span class="logo-mark"></span>Quillbrook.com</div>
  <nav class="main-nav">
    <a class="active" href="#">Home</a><a href="#">About</a><a href="#">Services</a><a href="#">Portfolio</a><a href="#">Blog</a><a href="#">Contact Us</a>
  </nav>
  <div class="contact-strip">
    <span><svg width="14" height="14" viewBox="0 0 24 24"><path fill="#fff" d="M6.6 10.8a15 15 0 0 0 6.6 6.6l2.2-2.2a1 1 0 0 1 1-.25 11 11 0 0 0 3.6.6 1 1 0 0 1 1 1V20a1 1 0 0 1-1 1A17 17 0 0 1 3 4a1 1 0 0 1 1-1h3.5a1 1 0 0 1 1 1 11 11 0 0 0 .6 3.6 1 1 0 0 1-.25 1z"/></svg>01632 960 418</span>
    <span><svg width="16" height="12" viewBox="0 0 16 12"><rect x="0.5" y="0.5" width="15" height="11" fill="none" stroke="#fff"/><path d="M1 1l7 6 7-6" fill="none" stroke="#fff"/></svg>info@quillbrook.com</span>
  </div>
</header>

<section class="hero" role="img" aria-label="Photograph of printed business cards fanned on a desk">
  <div class="hero-badge">STICKERS &amp;<br>LABEL<br>PRINTING</div>
  <div class="slider-dots"><i class="on"></i><i></i><i></i></div>
</section>

<section class="products">
  <div class="wrap">
    <div class="row-head">
      <h2>Select our popular products</h2>
      <div class="arrows">
        <span class="prev"><svg width="10" height="12" viewBox="0 0 10 12"><path d="M8 1L2 6l6 5z" fill="#fff"/></svg></span>
        <span class="next"><svg width="10" height="12" viewBox="0 0 10 12"><path d="M2 1l6 5-6 5z" fill="#fff"/></svg></span>
      </div>
    </div>
    <div class="product-row">
      <div class="product-tile tile-cards" role="img" aria-label="Photograph of dark business cards"></div>
      <div class="product-tile tile-flyers"><strong>A4 FLYERS</strong><b>£57</b><a href="#">View All Details</a></div>
      <div class="product-tile tile-letterhead" role="img" aria-label="Photograph of letterhead stationery"></div>
      <div class="product-tile tile-leaflet" role="img" aria-label="Photograph of printed leaflets"></div>
      <div class="product-tile tile-brochure" role="img" aria-label="Photograph of an open brochure"></div>
    </div>
  </div>
</section>

<section class="design-team" role="img" aria-label="Photograph of a designer working at a desk">
  <h2>Inhous  Design Team</h2>
  <p>Quillbrook.com offer a low cost design service with a fixed fee. To see our price list</p>
  <a class="btn-outline" href="#">Click Here</a>
</section>

<section class="portfolio">
  <div class="wrap">
    <h2 class="title">View Our Portfolio</h2>
    <div class="row-head">
      <h3>Website Designs</h3>
      <div class="arrows">
        <span class="prev"><svg width="10" height="12" viewBox="0 0 10 12"><path d="M8 1L2 6l6 5z" fill="#fff"/></svg></span>
        <span class="next"><svg width="10" height="12" viewBox="0 0 10 12"><path d="M2 1l6 5-6 5z" fill="#fff"/></svg></span>
      </div>
    </div>
    <div class="folio-row">
      <div class="folio-tile folio-blue"><div class="template-label">Template Name</div></div>
      <div class="folio-tile folio-cafe" role="img" aria-label="Screenshot of a coffee shop website"></div>
      <div class="folio-tile folio-office" role="img" aria-label="Screenshot of a business services website"></div>
      <div class="folio-tile folio-fitness" role="img" aria-label="Screenshot of a fitness studio website"></div>
    </div>
    <div class="row-head second">
      <h3>Charity Flyers</h3>
      <div class="arrows">
        <span class="prev"><svg width="10" height="12" viewBox="0 0 10 12"><path d="M8 1L2 6l6 5z" fill="#fff"/></svg></span>
        <span class="next"><svg width="10" height="12" viewBox="0 0 10 12"><path d="M2 1l6 5-6 5z" fill="#fff"/></svg></span>
      </div>
    </div>
    <div class="folio-row">
      <div class="folio-tile folio-flyer" role="img" aria-label="Charity event flyer design"></div>
      <div class="folio-tile folio-teal"><div class="template-label">Template Name</div></div>
      <div class="folio-tile folio-heart" role="img" aria-label="Charity event flyer with heart artwork"></div>
      <div class="folio-tile folio-run" role="img" aria-label="Charity fun run flyer design"></div>
    </div>
  </div>
  <a class="view-all" href="#">View All</a>
</section>

<section class="blog">
  <svg class="bands" width="1200" height="520" viewBox="0 0 1200 520">
    <polygon points="0,0 420,0 0,300" fill="#4cb6e2"/>
    <polygon points="1200,0 760,0 1200,320" fill="#2b98c9"/>
    <polygon points="0,520 0,330 520,520" fill="#2b98c9"/>
    <polygon points="1200,520 1200,340 700,520" fill="#4cb6e2"/>
  </svg>
  <h2>Blog</h2>
  <div class="wrap">
    <div class="blog-row">
      <article class="post">
        <div class="post-img post-1" role="img" aria-label="Photograph of a printed city skyline wallpaper"></div>
        <div class="post-date">10 April 2015</div>
        <a class="post-title" href="#">Digital Wallpaper Now Offered</a>
      </article>
      <article class="post">
        <div class="post-img post-2" role="img" aria-label="Photograph of an exhibition stand"></div>
        <div class="post-date">10 April 2015</div>
        <a class="post-title" href="#">North East Expo</a>
      </article>
      <article class="post">
        <div class="post-img post-3" role="img" aria-label="Photograph of a giant charity cheque presentation"></div>
        <div class="post-date">10 April 2015</div>
        <a class="post-title" href="#">In the money - charity cheque printing</a>
      </article>
    </div>
  </div>
</section>

<section class="newsletter">
  <h2>NewsLetter</h2>
  <form class="signup"><input type="text" value="email id"><button type="button">Subscribe</button></form>
</section>

<footer class="site-footer">
  <div class="wrap">
    <div class="footer-cols">
      <div class="footer-col">
        <h4>Latest News</h4>
        <div class="news-item"><span class="news-thumb"></span><p>Lorem Ipsum is simply dummy Text. <a href="#">Read More</a></p></div>
        <div class="news-item"><span class="news-thumb"></span><p>Lorem Ipsum is simply dummy Text. <a href="#">Read More</a></p></div>
        <div class="news-item"><span class="news-thumb"></span><p>Lorem Ipsum is simply dummy Text. <a href="#">Read More</a></p></div>
      </div>
      <div class="footer-col">
        <h4>Important Links</h4>
        <ul class="links">
          <li>Flyer Printing</li><li>Folded Flyers</li><li>Brochure Printing</li><li>Poster Printing</li><li>Business Cards</li><li>Letterhead Printing</li><li>Compliment Slips</li><li>Mailing Services</li><li>Vinyl Banners &amp; Pull Ups</li><li>Stickers and Labels</li><li>Presentation Folders</li><li>Christmas Cards</li>
        </ul>
      </div>
      <div class="footer-col">
        <h4>Payment Option</h4>
        <div class="cards"><i></i><i></i><i></i><i></i><i></i><i></i><i></i><i></i></div>
      </div>
      <div class="footer-col touch">
        <h4>Keep in Touch</h4>
        <p><svg width="14" height="18" viewBox="0 0 14 18"><path d="M7 0a7 7 0 0 0-7 7c0 5 7 11 7 11s7-6 7-11a7 7 0 0 0-7-7zm0 9.5A2.5 2.5 0 1 1 7 4.5a2.5 2.5 0 0 1 0 5z" fill="#fff"/></svg>Quillbrook.com Limited<br>Unit 4 Harrow Trade Park<br>Elmbridge<br>North Yarrow<br>NY4 7QB</p>
        <p><svg width="14" height="14" viewBox="0 0 24 24"><path fill="#fff" d="M6.6 10.8a15 15 0 0 0 6.6 6.6l2.2-2.2a1 1 0 0 1 1-.25 11 11 0 0 0 3.6.6 1 1 0 0 1 1 1V20a1 1 0 0 1-1 1A17 17 0 0 1 3 4a1 1 0 0 1 1-1h3.5a1 1 0 0 1 1 1 11 11 0 0 0 .6 3.6 1 1 0 0 1-.25 1z"/></svg>01632 960 418</p>
        <p><svg width="16" height="12" viewBox="0 0 16 12"><rect x="0.5" y="0.5" width="15" height="11" fill="none" stroke="#fff"/><path d="M1 1l7 6 7-6" fill="none" stroke="#fff"/></svg>info@quillbrook.com</p>
        <div class="social"><i></i><i></i><i></i></div>
      </div>
    </div>
  </div>
  <div class="footer-bottom">
    <nav><a href="#">Special Offers</a><a href="#">Terms and Conditions</a><a href="#">Privacy Policy</a><a href="#">Trade Account</a></nav>
    <p>Registered in England and Wales. Company Registration Number: 00000000. VAT Registration Number: 000 0000 00</p>
  </div>
</footer>

</body>
</html>
```